Automotive component supplier needs a business card design

We need a business card design for our company called Velmar Global Components Ltd based in the UK. We are a supplier of interior and exterior components to premium car manufacturers such as Corvane Hale, Durrant Fyfe, Maxtorn and Valdessimo. We would like to see a modern business card design that uses the colour blue.

Target Market(s)

Premium automotive car manufacturers.

Industry/Entity Type

Automotive

Contact Information for Business Card

Company Name : Velmar Global Components Limited
Address: 17 Tamsey Yard, Upper Drisk, Warwick, CV31 8RJ, United Kingdom
Web Address : www.velmarparts-example.co.uk

Font styles to use
Other font styles liked:
• Helvetica

Colors
3176b5
0255a3
85acd3
cfdeed
cee9f5
85cae6
34a6d7
0692cd
9bcb3c

Requirements
Must have
• Clear company logo and a mixture of blue colours.
Nice to have
• A high quality modern image.
Should not have
• Multiple colours.

```html
<!DOCTYPE html>
<html lang="en">
<head>
<meta charset="utf-8">
<title>Velmar Global Components – Business Card</title>
<link rel="stylesheet" href="https://fonts.googleapis.com/css2?family=Lato:wght@300;400;700&family=Montserrat:wght@700&display=swap">
<style>
  :root {
    --blue-deep: #0255a3;
    --blue-mid: #1d5fb5;
    --blue-bright: #0692cd;
    --green: #9bcb3c;
    --ink: #1b1b1b;
    --icon-dark: #0c2a4a;
    --paper: #f4f4f2;
    --paper-back: #fbfbfb;
    --backdrop: #e6e8eb;
  }
  * { margin: 0; padding: 0; box-sizing: border-box; }
  html, body { width: 1200px; height: 873px; overflow: hidden; }
  body {
    background: var(--backdrop);
    font-family: "Lato", Helvetica, Arial, sans-serif;
    display: flex;
    flex-direction: column;
    align-items: center;
    justify-content: center;
    gap: 56px;
  }
  .card {
    position: relative;
    width: 560px;
    height: 320px;
    overflow: hidden;
    box-shadow: 0 6px 18px rgba(0,0,0,0.12);
  }
  .card svg.shapes { position: absolute; inset: 0; }

  /* Front */
  .card-front { background: var(--paper); }
  .brand {
    position: absolute;
    display: flex;
    align-items: center;
    gap: 10px;
    color: var(--blue-bright);
    font-weight: 700;
    white-space: nowrap;
  }
  .brand-dot {
    width: 12px; height: 12px; border-radius: 50%;
    background: var(--green);
  }
  .card-front .brand { top: 44px; right: 44px; font-size: 22px; }
  .holder { position: absolute; right: 38px; top: 196px; text-align: right; }
  .holder-name {
    font-family: "Montserrat", Helvetica, Arial, sans-serif;
    font-weight: 700;
    font-size: 27px;
    letter-spacing: 2px;
    color: var(--ink);
  }
  .holder-phone {
    margin-top: 6px;
    font-size: 14px;
    color: var(--ink);
    display: flex; align-items: center; justify-content: flex-end; gap: 8px;
  }
  .contact {
    position: absolute;
    left: 20px; top: 192px;
    width: 272px;
    color: #fff;
    font-weight: 300;
    font-size: 13px;
    line-height: 1.35;
  }
  .contact-row {
    display: flex; align-items: center; justify-content: flex-end;
    gap: 10px; text-align: right; margin-bottom: 8px;
  }
  .icon { width: 24px; height: 24px; flex: none; }

  /* Back */
  .card-back { background: var(--paper-back); }
  .card-back .brand {
    left: 0; right: 0; top: 118px;
    justify-content: center;
    font-size: 34px;
  }
  .card-back .brand-dot { width: 18px; height: 18px; }
  .back-web {
    position: absolute;
    left: 0; right: 0; bottom: 20px;
    text-align: center;
    color: #fff;
    font-weight: 700;
    font-size: 15px;
    letter-spacing: 0.5px;
  }
</style>
</head>
<body>

<section class="card card-front" aria-label="Business card front">
  <svg class="shapes" width="560" height="320" viewBox="0 0 560 320">
    <polygon points="0,130 300,130 390,320 0,320" fill="var(--blue-mid)"/>
    <polygon points="300,158 311,158 379,320 368,320" fill="var(--green)"/>
  </svg>

  <div class="brand"><span class="brand-dot"></span>Velmar Global Components</div>

  <div class="holder">
    <div class="holder-name">MY NAME</div>
    <div class="holder-phone">
      +1234567890
      <svg class="icon" viewBox="0 0 24 24" aria-hidden="true">
        <circle cx="12" cy="12" r="12" fill="var(--green)"/>
        <path d="M9 6.5c.6 0 1 .3 1.2.8l.7 1.8c.2.5 0 1-.4 1.3l-.8.6c.6 1.4 1.7 2.5 3.1 3.2l.6-.8c.3-.4.9-.6 1.3-.4l1.8.7c.5.2.8.6.8 1.2v1.3c0 .7-.6 1.2-1.3 1.1C10.6 16.7 7.3 13.4 7 8.9c0-.7.5-1.3 1.2-1.3z" fill="var(--icon-dark)"/>
      </svg>
    </div>
  </div>

  <div class="contact">
    <div class="contact-row">
      <span>myemail@velmar-example.co.uk</span>
      <svg class="icon" viewBox="0 0 24 24" aria-hidden="true">
        <circle cx="12" cy="12" r="12" fill="var(--icon-dark)"/>
        <path d="M12 5a4.5 4.5 0 0 0-4.5 4.5c0 3.3 4.5 8.5 4.5 8.5s4.5-5.2 4.5-8.5A4.5 4.5 0 0 0 12 5zm0 6.3a1.8 1.8 0 1 1 0-3.6 1.8 1.8 0 0 1 0 3.6z" fill="var(--green)"/>
      </svg>
    </div>
    <div class="contact-row">
      <span>17 Tamsey Yard, Upper Drisk,<br>Warwick, CV31 8RJ, United Kingdom</span>
      <svg class="icon" viewBox="0 0 24 24" aria-hidden="true">
        <circle cx="12" cy="12" r="12" fill="var(--icon-dark)"/>
        <path d="M12 5a4.5 4.5 0 0 0-4.5 4.5c0 3.3 4.5 8.5 4.5 8.5s4.5-5.2 4.5-8.5A4.5 4.5 0 0 0 12 5zm0 6.3a1.8 1.8 0 1 1 0-3.6 1.8 1.8 0 0 1 0 3.6z" fill="var(--green)"/>
      </svg>
    </div>
    <div class="contact-row">
      <span>www.velmarparts-example.co.uk</span>
      <svg class="icon" viewBox="0 0 24 24" aria-hidden="true">
        <circle cx="12" cy="12" r="12" fill="var(--icon-dark)"/>
        <g fill="none" stroke="var(--green)" stroke-width="1.4">
          <circle cx="12" cy="12" r="6.5"/>
          <ellipse cx="12" cy="12" rx="2.8" ry="6.5"/>
          <line x1="5.5" y1="12" x2="18.5" y2="12"/>
          <line x1="6.5" y1="8.8" x2="17.5" y2="8.8"/>
          <line x1="6.5" y1="15.2" x2="17.5" y2="15.2"/>
        </g>
      </svg>
    </div>
  </div>
</section>

<section class="card card-back" aria-label="Business card back">
  <svg class="shapes" width="560" height="320" viewBox="0 0 560 320">
    <rect x="0" y="0" width="560" height="18" fill="var(--blue-mid)"/>
    <polygon points="0,300 90,300 120,262 440,262 470,300 560,300 560,320 0,320" fill="var(--blue-mid)"/>
  </svg>
  <div class="brand"><span class="brand-dot"></span>Velmar Global Components</div>
  <div class="back-web">www.velmarparts-example.co.uk</div>
</section>

</body>
</html>
```